Luxury Brand Real Estate For Sale sign

**Update** I've added some examples from the internet of other signs that have a look similar to what I would like to see. I do not want my personal name in the sign. And the word FOR SALE Does not need to be so large - it can be more subtle.
I want to create a Real Estate for sale sign for my company that will be used for luxury/higher end real estate listings. I’m sharing my business card as well as a logo with new teal color to show what we're moving towards: we’re using Teal, white, black and gold.
Hoping the sign is simple, sophisticated and eye catching.
The sign should be 24" wide by 30" tall including the company name: Harbor Crest Realty Group and our logo, office phone number 727-555-0148 and website www.hcrgexample.com the words "For Sale"
Optional to add this e-mail address info@hcrgexample.com to the sign
Target Market(s)
Luxury home buyers
Industry/Entity Type
Real Estate
Look and feel

```html
<!DOCTYPE html>
<html lang="en">
<head>
<meta charset="utf-8">
<title>Harbor Crest Realty Group – For Sale Sign</title>
<link href="https://fonts.googleapis.com/css2?family=Montserrat:wght@300;600&family=Quicksand:wght@400&display=swap" rel="stylesheet">
<style>
  :root {
    --teal: #2b847a;
    --night: #1b1c1e;
    --ink: #1b1b1b;
    --ink-warm: #302a2a;
    --paper: #ffffff;
  }
  * { margin: 0; padding: 0; box-sizing: border-box; }
  html, body {
    width: 1200px;
    height: 1200px;
    overflow: hidden;
    background: var(--paper);
  }
  body { display: flex; }
  .panel {
    position: relative;
    width: 600px;
    height: 1200px;
    display: flex;
    align-items: center;
    justify-content: center;
  }
  .panel--dark { background: var(--night); }
  .panel--light { background: var(--paper); }

  /* 24" x 30" portrait sign */
  .sign {
    position: relative;
    width: 480px;
    height: 600px;
    background: var(--paper);
    border: 12px solid var(--teal);
    display: flex;
    flex-direction: column;
    align-items: center;
    padding-top: 62px;
  }
  .brand__mark {
    width: 96px;
    height: 96px;
    border: 4px solid var(--teal);
  }
  .brand__name {
    margin-top: 34px;
    font-family: "Montserrat", sans-serif;
    font-weight: 300;
    font-size: 30px;
    line-height: 38px;
    letter-spacing: 1px;
    color: var(--teal);
    text-transform: uppercase;
    text-align: center;
    white-space: nowrap;
  }
  .brand__divider {
    margin-top: 34px;
    width: 140px;
    height: 3px;
    background: var(--ink);
  }
  .listing__status {
    margin-top: 40px;
    font-family: "Montserrat", sans-serif;
    font-weight: 600;
    font-size: 36px;
    line-height: 1;
    letter-spacing: 6px;
    color: var(--ink-warm);
    text-transform: uppercase;
  }
  .contact {
    font-family: "Quicksand", sans-serif;
    font-weight: 400;
    color: var(--ink);
    text-align: center;
    white-space: nowrap;
  }
  .contact--phone { margin-top: 34px; font-size: 17px; }
  .contact--phone .contact__value { font-size: 24px; margin-left: 10px; }
  .contact--web { margin-top: 12px; font-size: 18px; }

  .sign--mono .brand__mark { border-color: var(--ink); }
  .sign--mono .brand__name { color: var(--ink); }
  .sign--mono .listing__status { color: var(--ink); }
</style>
</head>
<body>

<section class="panel panel--dark">
  <div class="sign">
    <div class="brand__mark"></div>
    <div class="brand__name">Harbor Crest<br>Realty Group</div>
    <div class="brand__divider"></div>
    <div class="listing__status">For Sale</div>
    <p class="contact contact--phone">phone number<span class="contact__value">727-555-0148</span></p>
    <p class="contact contact--web">website www.hcrgexample.com</p>
  </div>
</section>

<section class="panel panel--light">
  <div class="sign sign--mono">
    <div class="brand__mark"></div>
    <div class="brand__name">Harbor Crest<br>Realty Group</div>
    <div class="brand__divider"></div>
    <div class="listing__status">For Sale</div>
    <p class="contact contact--phone">phone number<span class="contact__value">727-555-0148</span></p>
    <p class="contact contact--web">website www.hcrgexample.com</p>
  </div>
</section>

</body>
</html>
```